New website for existing IT services company

We are a leading IT managed services provider and cloud services provider based in Sydney, Australia.
We are looking for a fresh, modern, contemporary and functional website.
We need a certain level of dynamic capabilities, such as the option to add youtube training / blog clips. So there needs to be a CMS.
Our existing website has pages including home, about us, services, contact us. Also links for remote support and connecting to our help desk system. As well as client testimonials.
The existing website is korivel.com.au however this is only posted for informational purposes. We are looking at a complete fresh re-design
We are open to the use of illustrations, however this is not a must.
I have uploaded an eps file containing our logo.
Updates
The website needs to be functional on tablets and phones as well. Added Thursday, April 30, 2015

```html
<!DOCTYPE html>
<html lang="en">
<head>
<meta charset="utf-8">
<title>Korivel – IT Services</title>
<link href="https://fonts.googleapis.com/css2?family=Roboto:wght@300;400;700&display=swap" rel="stylesheet">
<style>
  :root {
    --sky: #3ec6f2;
    --ink: #0a0a0a;
    --white: #ffffff;
    --navy-deep: #030a3a;
    --navy-mid: #0b2f6e;
    --teal: #2f8fb8;
    --key-grey: #6e7479;
    --key-dark: #2b2e31;
    --key-blue: #4aa3c8;
  }
  * { box-sizing: border-box; margin: 0; padding: 0; }
  html, body {
    width: 1200px; height: 1000px; overflow: hidden;
    font-family: "Roboto", "Helvetica Neue", Arial, sans-serif;
    background: var(--white);
  }
  .site { position: relative; width: 1200px; height: 1000px; }

  .site-header {
    position: absolute; left: 0; top: 0; width: 1200px; height: 132px;
    background: var(--sky);
  }
  .brand {
    position: absolute; left: 28px; top: 28px;
    display: flex; align-items: center; gap: 14px;
  }
  .brand-name {
    font-size: 62px; font-weight: 700; color: var(--ink);
    letter-spacing: -1px; line-height: 1;
  }
  .brand-mark {
    width: 26px; height: 26px; border: 3px solid var(--ink);
  }
  .main-nav {
    position: absolute; top: 72px; left: 0; width: 1200px; height: 37px;
  }
  .main-nav a {
    position: absolute; top: 0; height: 37px; line-height: 37px;
    font-size: 24px; font-weight: 400; color: var(--white);
    text-decoration: none; text-align: center;
  }
  .main-nav a.is-active {
    background: var(--white); color: var(--sky); padding: 0 10px;
  }

  .hero {
    position: absolute; left: 0; top: 132px; width: 1200px; height: 615px;
    overflow: hidden;
  }
  .hero-photo {
    position: absolute; inset: 0;
    background:
      radial-gradient(ellipse 420px 300px at 560px 260px, rgba(60,150,200,0.55), transparent 70%),
      radial-gradient(ellipse 200px 260px at 150px 260px, rgba(70,180,230,0.5), transparent 70%),
      linear-gradient(100deg, var(--navy-mid) 0%, var(--navy-deep) 55%, #071a55 100%);
  }
  .hero-title {
    position: absolute; left: 0; top: 128px; width: 1200px;
    text-align: center; color: var(--white);
    font-weight: 300; font-size: 60px; line-height: 66px;
  }
  .hero-title span { display: block; }
  .hero-title .line-1 { padding-left: 12px; }

  .service-list { position: absolute; left: 0; top: 375px; width: 1200px; }
  .service {
    position: absolute; top: 0; width: 160px; margin-left: -80px;
    text-align: center; color: var(--white);
  }
  .service-ring {
    width: 130px; height: 130px; margin: 0 auto;
    border: 2px solid var(--white); border-radius: 50%;
    display: flex; align-items: center; justify-content: center;
  }
  .service-label {
    margin-top: 12px; font-size: 16px; line-height: 19px; font-weight: 400;
  }

  .shop-band {
    position: absolute; left: 0; top: 747px; width: 1200px; height: 253px;
    background:
      linear-gradient(100deg, transparent 0%, transparent 42%, var(--key-blue) 43%, #3d8fb4 85%, transparent 86%),
      linear-gradient(180deg, var(--key-grey) 0%, var(--key-dark) 100%);
  }
</style>
</head>
<body>
<div class="site">

  <header class="site-header">
    <div class="brand">
      <span class="brand-name">KORIVEL</span>
      <span class="brand-mark"></span>
    </div>
    <nav class="main-nav">
      <a href="#" style="left:404px">Home</a>
      <a href="#" style="left:511px">About</a>
      <a href="#" class="is-active" style="left:609px;width:110px">Services</a>
      <a href="#" style="left:760px">Store</a>
      <a href="#" style="left:848px">Contact</a>
      <a href="#" style="left:963px">Blog</a>
    </nav>
  </header>

  <section class="hero">
    <div class="hero-photo" role="img" aria-label="Blue-tinted photo of a man touching a tablet beside a desktop monitor"></div>

    <h1 class="hero-title">
      <span class="line-1">We Help You Connect to the World</span>
      <span>We love you , xxx you</span>
    </h1>

    <div class="service-list">
      <div class="service" style="left:196px">
        <div class="service-ring">
          <svg width="62" height="56" viewBox="0 0 62 56"><path d="M31 54 C10 38 2 28 2 16 C2 7 9 1 17 1 C23 1 28 4 31 9 C34 4 39 1 45 1 C53 1 60 7 60 16 C60 28 52 38 31 54Z" fill="#fff"/></svg>
        </div>
        <p class="service-label">Outsourced<br>IT Services</p>
      </div>

      <div class="service" style="left:402px">
        <div class="service-ring">
          <svg width="62" height="44" viewBox="0 0 62 44"><rect x="1" y="1" width="60" height="42" rx="2" fill="#fff"/><path d="M2 3 L31 26 L60 3" fill="none" stroke="#c9ccd0" stroke-width="2"/></svg>
        </div>
        <p class="service-label">Managed<br>Exchange</p>
      </div>

      <div class="service" style="left:608px">
        <div class="service-ring">
          <svg width="62" height="62" viewBox="0 0 62 62"><path d="M16 24 L31 6 L46 24" fill="none" stroke="#fff" stroke-width="4"/><rect x="2" y="22" width="58" height="9" fill="#fff"/><path d="M7 33 H55 L50 60 H12Z" fill="#fff"/><g stroke="#0b2f6e" stroke-width="3"><line x1="22" y1="38" x2="23" y2="54"/><line x1="31" y1="38" x2="31" y2="54"/><line x1="40" y1="38" x2="39" y2="54"/></g></svg>
        </div>
        <p class="service-label">Shop<br>Online</p>
      </div>

      <div class="service" style="left:806px">
        <div class="service-ring">
          <svg width="68" height="68" viewBox="0 0 68 68" fill="none" stroke="#fff" stroke-width="4"><circle cx="34" cy="34" r="31"/><ellipse cx="34" cy="34" rx="13" ry="31"/><line x1="34" y1="3" x2="34" y2="65"/><line x1="3" y1="34" x2="65" y2="34"/><line x1="8" y1="19" x2="60" y2="19"/><line x1="8" y1="49" x2="60" y2="49"/></svg>
        </div>
        <p class="service-label">Internet<br>Service</p>
      </div>

      <div class="service" style="left:1004px">
        <div class="service-ring">
          <svg width="72" height="72" viewBox="0 0 72 72"><g fill="#fff"><circle cx="26" cy="46" r="17"/><g stroke="#fff" stroke-width="8"><line x1="26" y1="24" x2="26" y2="68"/><line x1="4" y1="46" x2="48" y2="46"/><line x1="10" y1="30" x2="42" y2="62"/><line x1="42" y1="30" x2="10" y2="62"/></g><circle cx="54" cy="16" r="10"/><g stroke="#fff" stroke-width="5"><line x1="54" y1="2" x2="54" y2="30"/><line x1="40" y1="16" x2="68" y2="16"/><line x1="44" y1="6" x2="64" y2="26"/><line x1="64" y1="6" x2="44" y2="26"/></g></g><circle cx="26" cy="46" r="6" fill="#0a0a0a"/><circle cx="26" cy="46" r="2.5" fill="#fff"/><circle cx="54" cy="16" r="4" fill="#0a0a0a"/><circle cx="54" cy="16" r="1.5" fill="#fff"/></svg>
        </div>
        <p class="service-label">Hosted<br>Solutions</p>
      </div>
    </div>
  </section>

  <section class="shop-band" role="img" aria-label="Close-up photo of a laptop keyboard with a blue shopping-cart key"></section>

</div>
</body>
</html>
```